Cedar Row Maintenance and Concierge Flyer

We need a flyer for cedar row maintenance and concierge service. We specialize in and provide residential maintenance and errand services to retired and semi retired persons living in the Lake Norman area. The services we include:
Lighting and plumbing repairs
Ceiling fan installation
Handicap accessories
Locks and security
Picture hanging
Hang blinds
Furniture arrangement / assembly
Pressure washing
Battery Jump start
and more...

Our Concierge services include:
Errand running
Grocery shopping
Wellness Checks
Dog Walk
Garbage Collection
and more...

We offer monthly service agreements and 24/7 access
Call text or e-mail for more information
704.555.0187
1cedarrowmaint@quillpostmail.com

The design should invoke a sense of trust and a customer service driven mission

Target Market(s)

Residential maintenance

Industry/Entity Type

Property Maintenance

Contact Information for Business Card

Derek Halvorsen
48176 Quimby Ferrel Rd.
Cornelius NC 28031
704.555.0187
with uploaded logo

Requirements
Nice to have
• Would like a postcard size flyer. Front and back
Should not have
• No pics of of people wearing hard hats or pics of blueprints. No pics of commercial or industrial maintenance.

```html
<!DOCTYPE html>
<html lang="en">
<head>
<meta charset="utf-8">
<title>Cedar Row Maintenance and Concierge – Postcard Flyer</title>
<link href="https://fonts.googleapis.com/css2?family=Arimo:wght@400;700&family=Tangerine:wght@400&display=swap" rel="stylesheet">
<style>
  :root{
    --stage:#16628a;
    --paper:#ffffff;
    --ink:#333333;
    --ink-soft:#444444;
    --red:#e2343b;
    --grey:#6e6e6e;
    --orange:#f08a1c;
    --rose:#b9545a;
    --sky:#4a95c9;
    --azure:#3aa8df;
    --navy:#1a5aa0;
    --lime:#8dc63f;
    --aqua:#6ccbe8;
    --amber:#f07f1f;
    --gold:#f2c23c;
    --green:#15a36c;
    --banner-dark:#2f2f35;
  }
  *{box-sizing:border-box;margin:0;padding:0}
  html,body{width:845px;height:1200px;overflow:hidden;background:var(--stage)}
  body{font-family:"Arimo",Arial,sans-serif;color:var(--ink)}
  .stage{position:absolute;left:0;top:0;width:800px;height:1136px;transform:scale(1.05625);transform-origin:0 0}
  .side-label{position:absolute;left:0;width:780px;text-align:center;color:#fff;font-size:32px}
  .side-label--front{top:16px}
  .side-label--back{top:1062px}
  .card{position:absolute;left:35px;width:710px;height:473px;background:var(--paper)}
  .card--front{top:62px}
  .card--back{top:575px}
  .abs{position:absolute}

  .headline{left:0;top:24px;width:400px;text-align:center;font-size:34px;line-height:42px;color:var(--ink)}
  .headline strong{display:block;color:var(--red);font-weight:700}
  .intro{left:16px;top:127px;width:366px;font-size:11.3px;line-height:20px;color:var(--ink-soft);text-align:justify}
  .intro p+p{margin-top:20px}

  .brand{display:flex;align-items:center;gap:10px}
  .brand__mark{width:56px;height:56px;border-radius:50%;background:var(--red);flex:none}
  .brand__name{color:var(--grey);font-size:30px;line-height:32px}
  .brand__name small{display:block;font-size:13px;line-height:16px}
  .brand--front{left:42px;top:265px}
  .brand--back{left:405px;top:280px}
  .brand--back .brand__mark{width:44px;height:44px}
  .brand--back .brand__name{font-size:24px;line-height:26px}
  .brand--back .brand__name small{font-size:10px;line-height:12px}

  .contact{display:flex;align-items:center;gap:8px;font-weight:700;color:var(--ink)}
  .contact svg{flex:none}
  .phone-big{left:45px;top:365px;font-size:44px}
  .email-front{left:47px;top:412px;font-size:17px}

  .tiles{left:390px;top:36px;display:grid;grid-template-columns:repeat(3,88px);grid-auto-rows:88px;column-gap:17px;row-gap:19px}
  .tile{width:88px;height:88px}

  .list-title{font-size:15px;font-weight:700;color:var(--red);line-height:23px}
  .check-list{list-style:none;font-size:15.5px;line-height:22.7px;color:var(--ink)}
  .check-list li{display:flex;align-items:center;gap:5px}
  .check-list li.more{padding-left:17px}
  .services{left:26px;top:53px}
  .concierge{left:290px;top:53px}

  .bell-photo{left:435px;top:10px;width:275px;height:245px;background:radial-gradient(ellipse at 45% 65%,#c9c9c9 0%,#ececec 40%,#ffffff 70%)}

  .offer-band{left:205px;top:352px;width:505px;height:26px;background:linear-gradient(90deg,var(--banner-dark) 0%,var(--banner-dark) 45%,var(--red) 100%);clip-path:polygon(0 0,100% 0,100% 100%,0 100%,8px 50%);color:#fff;font-weight:700;font-size:16px;line-height:26px;padding-left:16px}
  .cta{left:150px;top:388px;width:233px;text-align:right;font-size:18.5px;font-weight:700;line-height:29px;color:var(--ink)}
  .divider{left:396px;top:387px;width:2px;height:53px;background:var(--ink)}
  .phone-back{left:415px;top:384px;font-size:34px}
  .email-back{left:418px;top:420px;font-size:14.5px}
</style>
</head>
<body>
<div class="stage">
  <div class="side-label side-label--front">front</div>

  <section class="card card--front">
    <h1 class="abs headline">When you're too busy,<strong>WE GET DONE.</strong></h1>
    <div class="abs intro">
      <p>Are you at your wits end trying to find time to get everything done in the limited fre time you have? Yes? Then&nbsp; Cedar Row can:</p>
      <p>Help you free up your time; do the routine tasks that take up valuable free time; so you can use your vacation/personal time for what is meant for- spending time. Cedar Row can help you</p>
    </div>

    <div class="abs brand brand--front">
      <span class="brand__mark"></span>
      <span class="brand__name">Cedar Row<small>MAINTENANCE &amp; CONCIERGE</small></span>
    </div>

    <div class="abs contact phone-big">
      <svg width="38" height="30" viewBox="0 0 38 30"><path d="M3 10c8-9 24-9 32 0l-2 6-7-2v-4c-4-1-8-1-12 0v4l-7 2z" fill="#e2343b"/><path d="M10 16h18l4 12H6z" fill="#e2343b"/><circle cx="19" cy="21" r="3.5" fill="#fff"/></svg>
      704.555.0187
    </div>
    <div class="abs contact email-front">
      <svg width="32" height="22" viewBox="0 0 32 22"><rect width="32" height="22" rx="2" fill="#e2343b"/><path d="M2 3l14 10L30 3M2 20l10-8M30 20l-10-8" stroke="#fff" stroke-width="2" fill="none"/></svg>
      1cedarrowmaint@quillpostmail.com
    </div>

    <div class="abs tiles">
      <div class="tile" style="background:var(--orange)" role="img" aria-label="Garbage bin icon"></div>
      <div class="tile" style="background:var(--rose)" role="img" aria-label="Armchair icon"></div>
      <div class="tile" style="background:var(--sky)" role="img" aria-label="Dripping faucet icon"></div>
      <div class="tile" style="background:var(--azure)" role="img" aria-label="Padlock icon"></div>
      <div class="tile" style="background:var(--navy)" role="img" aria-label="Wheelchair accessibility icon"></div>
      <div class="tile" style="background:var(--orange)" role="img" aria-label="Hanging light bulb icon"></div>
      <div class="tile" style="background:var(--lime)" role="img" aria-label="Ceiling fan icon"></div>
      <div class="tile" style="background:var(--aqua)" role="img" aria-label="Stethoscope icon"></div>
      <div class="tile" style="background:var(--amber)" role="img" aria-label="Grocery bag icon"></div>
      <div class="tile" style="background:var(--gold)" role="img" aria-label="Framed picture icon"></div>
      <div class="tile" style="background:var(--rose)" role="img" aria-label="Pressure washer spraying tiles icon"></div>
      <div class="tile" style="background:linear-gradient(160deg,#2cc28a,var(--green))" role="img" aria-label="Person walking a dog icon"></div>
    </div>
  </section>

  <section class="card card--back">
    <div class="abs bell-photo" role="img" aria-label="Photo of a hand pressing a silver service bell"></div>

    <div class="abs services">
      <h2 class="list-title">Services We Include:</h2>
      <ul class="check-list">
        <li><svg width="12" height="12" viewBox="0 0 12 12"><rect x=".5" y=".5" width="11" height="11" fill="none" stroke="#333"/><path d="M2.5 6l2.5 2.5 4.5-5" stroke="#333" stroke-width="1.5" fill="none"/></svg>Lighting and plumbing repairs</li>
        <li><svg width="12" height="12" viewBox="0 0 12 12"><rect x=".5" y=".5" width="11" height="11" fill="none" stroke="#333"/><path d="M2.5 6l2.5 2.5 4.5-5" stroke="#333" stroke-width="1.5" fill="none"/></svg>Ceiling fan installation</li>
        <li><svg width="12" height="12" viewBox="0 0 12 12"><rect x=".5" y=".5" width="11" height="11" fill="none" stroke="#333"/><path d="M2.5 6l2.5 2.5 4.5-5" stroke="#333" stroke-width="1.5" fill="none"/></svg>Handicap accessories</li>
        <li><svg width="12" height="12" viewBox="0 0 12 12"><rect x=".5" y=".5" width="11" height="11" fill="none" stroke="#333"/><path d="M2.5 6l2.5 2.5 4.5-5" stroke="#333" stroke-width="1.5" fill="none"/></svg>Locks and security</li>
        <li><svg width="12" height="12" viewBox="0 0 12 12"><rect x=".5" y=".5" width="11" height="11" fill="none" stroke="#333"/><path d="M2.5 6l2.5 2.5 4.5-5" stroke="#333" stroke-width="1.5" fill="none"/></svg>Picture hanging</li>
        <li><svg width="12" height="12" viewBox="0 0 12 12"><rect x=".5" y=".5" width="11" height="11" fill="none" stroke="#333"/><path d="M2.5 6l2.5 2.5 4.5-5" stroke="#333" stroke-width="1.5" fill="none"/></svg>Hang blinds</li>
        <li><svg width="12" height="12" viewBox="0 0 12 12"><rect x=".5" y=".5" width="11" height="11" fill="none" stroke="#333"/><path d="M2.5 6l2.5 2.5 4.5-5" stroke="#333" stroke-width="1.5" fill="none"/></svg>Furniture arrangement / assembly</li>
        <li><svg width="12" height="12" viewBox="0 0 12 12"><rect x=".5" y=".5" width="11" height="11" fill="none" stroke="#333"/><path d="M2.5 6l2.5 2.5 4.5-5" stroke="#333" stroke-width="1.5" fill="none"/></svg>Pressure washing</li>
        <li><svg width="12" height="12" viewBox="0 0 12 12"><rect x=".5" y=".5" width="11" height="11" fill="none" stroke="#333"/><path d="M2.5 6l2.5 2.5 4.5-5" stroke="#333" stroke-width="1.5" fill="none"/></svg>Battery Jump start, and more...</li>
      </ul>
    </div>

    <div class="abs concierge">
      <h2 class="list-title">Our Concierge<br>Services Include:</h2>
      <ul class="check-list">
        <li><svg width="12" height="12" viewBox="0 0 12 12"><rect x=".5" y=".5" width="11" height="11" fill="none" stroke="#333"/><path d="M2.5 6l2.5 2.5 4.5-5" stroke="#333" stroke-width="1.5" fill="none"/></svg>Errand running</li>
        <li><svg width="12" height="12" viewBox="0 0 12 12"><rect x=".5" y=".5" width="11" height="11" fill="none" stroke="#333"/><path d="M2.5 6l2.5 2.5 4.5-5" stroke="#333" stroke-width="1.5" fill="none"/></svg>Grocery shopping</li>
        <li><svg width="12" height="12" viewBox="0 0 12 12"><rect x=".5" y=".5" width="11" height="11" fill="none" stroke="#333"/><path d="M2.5 6l2.5 2.5 4.5-5" stroke="#333" stroke-width="1.5" fill="none"/></svg>Wellness Checks</li>
        <li><svg width="12" height="12" viewBox="0 0 12 12"><rect x=".5" y=".5" width="11" height="11" fill="none" stroke="#333"/><path d="M2.5 6l2.5 2.5 4.5-5" stroke="#333" stroke-width="1.5" fill="none"/></svg>Dog Walk</li>
        <li><svg width="12" height="12" viewBox="0 0 12 12"><rect x=".5" y=".5" width="11" height="11" fill="none" stroke="#333"/><path d="M2.5 6l2.5 2.5 4.5-5" stroke="#333" stroke-width="1.5" fill="none"/></svg>Garbage Collection,</li>
        <li class="more">and more...</li>
      </ul>
    </div>

    <div class="abs brand brand--back">
      <span class="brand__mark"></span>
      <span class="brand__name">Cedar Row<small>MAINTENANCE &amp; CONCIERGE</small></span>
    </div>

    <div class="abs offer-band">We offer monthly service agreements and 24/7 access</div>
    <p class="abs cta">Call text or e-mail<br>for more information</p>
    <div class="abs divider"></div>
    <div class="abs contact phone-back">
      <svg width="30" height="24" viewBox="0 0 38 30"><path d="M3 10c8-9 24-9 32 0l-2 6-7-2v-4c-4-1-8-1-12 0v4l-7 2z" fill="#e2343b"/><path d="M10 16h18l4 12H6z" fill="#e2343b"/><circle cx="19" cy="21" r="3.5" fill="#fff"/></svg>
      704.555.0187
    </div>
    <div class="abs contact email-back">
      <svg width="26" height="18" viewBox="0 0 32 22"><rect width="32" height="22" rx="2" fill="#e2343b"/><path d="M2 3l14 10L30 3M2 20l10-8M30 20l-10-8" stroke="#fff" stroke-width="2" fill="none"/></svg>
      1cedarrowmaint@quillpostmail.com
    </div>
  </section>

  <div class="side-label side-label--back">back</div>
</div>
</body>
</html>
```